Clothing Brand E-Commerce Website Design

We would like you to provide an ecommerce design template in layered PSD for our clothing/fashion brand website called "FernQuill".
We want the site to have a simple but sleek design similar to the following sites:
http://www.threadorbit.example/
http://tovalenwick.example/
http://www.sadiplume.example/
We want it to look stunning and blow the example sites out of the water. For color scheme, please use your imagination and try to impress us with your creativity.
We like teal and beige pink, with teal dominant.
Teal #7AFFFF / #46C6C6
Beige/pink #FF7B7C / #C74646
We want you to develop the design for 3 pages:
1) Home Page
Samples:
http://www.threadorbit.example/
http://tovalenwick.example/
http://www.sadiplume.example/
2) Products List Page (e.g., lists all "Dresses" when category is selected)
http://www.threadorbit.example/shop/casual-dresses
http://www.sadiplume.example/index.php?main_page=index&cPath=3
http://tovalenwick.example/modest-dresses.html
http://www.lunahive88.example/Product/Category.aspx?br=lh8&category=dress_maxi
3) Product Detail Page (e.g., individual product page with "Add to Cart")
http://www.threadorbit.example/shop/dresses/willow-dawn-dress
http://tovalenwick.example/modest-dresses/modest-dress-opal.html
http://www.sadiplume.example/index.php?main_page=product_info&cPath=3&products_id=297
Industry/Entity Type
Fashion

```html
<!DOCTYPE html>
<html lang="en">
<head>
<meta charset="utf-8">
<title>FernQuill — Home</title>
<link rel="stylesheet" href="https://fonts.googleapis.com/css2?family=Mulish:wght@300;400;600&family=Oswald:wght@500&display=swap">
<style>
:root{
  --teal:#46c6c6;
  --teal-bright:#6ff0f2;
  --dark:#404040;
  --text:#4a4a4a;
  --muted:#666;
  --line:#dcdcdc;
  --footer-bg:#efefef;
  --white:#fff;
}
*{box-sizing:border-box;margin:0;padding:0}
html,body{width:1130px;height:1200px;overflow:hidden;background:var(--white);font-family:"Mulish",sans-serif;color:var(--text)}
.page{position:relative;width:1130px;height:1200px}
a{color:inherit;text-decoration:none}
.abs{position:absolute}

/* header */
.brand{left:70px;top:30px;font-size:40px;font-weight:300;color:#555;letter-spacing:.5px}
.util-links{right:70px;top:21px;display:flex;gap:14px;font-size:11px;color:#666;letter-spacing:.3px;align-items:center}
.util-links .sep{color:#999}
.util-links svg{vertical-align:-2px;margin-right:5px}
.search{left:833px;top:54px;width:227px;height:28px;border:1px solid var(--line);background:#fafafa;font-size:11px;color:#999;padding:7px 12px}
.search svg{position:absolute;right:8px;top:6px}

/* nav */
.main-nav{left:70px;top:100px;width:991px;height:45px;background:var(--teal);display:flex;justify-content:space-around;align-items:center;color:var(--white);font-size:14px;letter-spacing:.3px}

/* sidebar */
.panel-head{left:70px;width:240px;height:41px;background:var(--dark);color:var(--white);font-size:16px;padding:13px 16px;letter-spacing:.3px}
.cat-list{left:70px;top:194px;width:240px;height:223px;background:var(--teal);list-style:none;padding-top:8px}
.cat-list li{height:34px;padding-left:16px;display:flex;align-items:center;color:var(--white);font-size:14px}
.cat-list li::before{content:"→";font-size:8px;margin-right:10px}
.perk{left:70px;width:240px;height:75px;background:var(--dark);display:flex;align-items:center;padding-left:16px}
.perk svg{flex:none;width:60px;height:50px;margin-right:18px}
.perk h3{font-weight:400;font-size:19px;color:var(--teal-bright)}
.perk p{font-size:11px;color:var(--teal-bright);margin-top:2px}
.newsletter{left:70px;top:735px;width:240px;height:188px;background:var(--teal);padding:14px 16px;color:var(--white)}
.newsletter p{font-size:13px;line-height:17px}
.newsletter .email{margin-top:18px;height:34px;background:var(--white);border:1px solid #e5e5e5;color:#777;font-size:10.5px;padding:11px 10px}
.newsletter .subscribe{position:absolute;right:21px;bottom:31px;width:99px;height:29px;background:var(--teal-bright);color:#2d5d5d;font-size:12px;display:flex;align-items:center;justify-content:center;border:1px solid #fff}

/* hero */
.hero{left:323px;top:154px;width:737px;height:334px;border:1px solid var(--line);overflow:hidden;background:linear-gradient(90deg,#5a4060 0%,#8a6c78 30%,#c9d6df 60%,#9aa9b3 100%)}
.hero-title{position:absolute;left:438px;top:92px;font-family:"Oswald",sans-serif;font-weight:500;line-height:88px;font-size:100px;letter-spacing:-1px}
.hero-title span{display:block}
.hero-title .mega{color:#111}
.hero-title .sale{color:#4a5a70;padding-left:56px}
.dots{position:absolute;left:17px;top:300px;display:flex;gap:6px}
.dots i{width:15px;height:15px;border-radius:3px;background:#111}
.dots i.on{background:var(--teal)}

/* featured */
.section-title{left:323px;top:512px;width:737px;text-align:center;font-size:21px;font-weight:400;color:#444}
.card{top:556px;width:228px;height:367px;border:1px solid var(--line);text-align:center}
.card .photo{margin:9px auto 0;width:120px;height:222px}
.card h4{font-weight:400;font-size:16.5px;color:var(--teal);margin-top:10px}
.card p{font-size:13px;line-height:17.5px;color:var(--text);padding:0 24px;margin-top:3px}
.card .shop{display:inline-flex;width:101px;height:30px;margin-top:13px;background:var(--teal-bright);color:#2d5d5d;font-size:12px;align-items:center;justify-content:center;border:1px solid var(--teal)}

/* footer */
.footer{left:0;top:956px;width:1130px;height:193px;background:var(--footer-bg)}
.foot-col{top:984px}
.foot-col h5{font-weight:400;font-size:14px;color:var(--teal);margin-bottom:6px}
.foot-col li{list-style:none;font-size:11px;color:#555;height:22px;display:flex;align-items:center}
.foot-col.social li{height:27px}
.foot-col.social i{width:13px;height:13px;border-radius:2px;margin-right:9px;display:inline-block}
.copyright{left:0;top:1149px;width:1130px;height:51px;background:var(--teal);color:var(--white);font-size:12px;padding:19px 70px}
.copyright b{font-weight:400;color:#2f4f4f}
</style>
</head>
<body>
<div class="page">

  <header>
    <a class="abs brand" href="#">FernQuill</a>
    <nav class="abs util-links">
      <a href="#">SIGN IN</a><span class="sep">|</span>
      <a href="#">MY ACCOUNT</a><span class="sep">|</span>
      <a href="#"><svg width="11" height="12" viewBox="0 0 11 12"><path d="M1 4h9l-.6 8H1.6z" fill="#666"/><path d="M3.5 4V3a2 2 0 014 0v1" stroke="#666" fill="none"/></svg>MY BAG</a><span class="sep">|</span>
      <a href="#">CHECKOUT</a>
    </nav>
    <div class="abs search">Search..
      <svg width="16" height="16" viewBox="0 0 16 16"><circle cx="6" cy="6" r="4.5" stroke="#999" stroke-width="1.6" fill="none"/><path d="M9.5 9.5l5 4" stroke="#999" stroke-width="2.4"/></svg>
    </div>
  </header>

  <nav class="abs main-nav">
    <a href="#">HOME</a><a href="#">NEW!</a><a href="#">TOPS</a><a href="#">BOTTOMS</a><a href="#">DRESSES</a><a href="#">ACCESSORIES</a><a href="#">CLEARANCE</a><a href="#">BLOG</a><a href="#">CONTACT</a>
  </nav>

  <aside>
    <div class="abs panel-head" style="top:153px">CATEGORIES</div>
    <ul class="abs cat-list">
      <li>Dresses</li><li>Tops/Skirts→</li><li>Style by Juniper→</li><li>Clearance</li><li>Gift Certificates</li><li>Accessories→</li>
    </ul>

    <div class="abs perk" style="top:431px">
      <svg viewBox="0 0 60 50"><rect x="4" y="10" width="30" height="26" fill="#fff"/><path d="M36 18h12l8 10v8H36z" fill="#fff"/><circle cx="14" cy="40" r="5" fill="#fff" stroke="#404040" stroke-width="2"/><circle cx="46" cy="40" r="5" fill="#fff" stroke="#404040" stroke-width="2"/><path d="M19 30V20h-5l7-7 7 7h-5v10z" fill="#404040"/></svg>
      <div><h3>FREE Shipping</h3><p>on Orders $50+ »</p></div>
    </div>
    <div class="abs perk" style="top:518px">
      <svg viewBox="0 0 60 50"><path d="M6 26L20 8l14 18h-8c0 8 4 14 10 18-12 0-18-8-18-18z" fill="#fff"/><path d="M54 24L40 42 26 24h8c0-8-4-14-10-18 12 0 18 8 18 18z" fill="#fff"/></svg>
      <div><h3>FREE Exchange</h3><p>&amp; Easy Returns!</p></div>
    </div>
    <div class="abs perk" style="top:607px">
      <svg viewBox="0 0 60 50"><path d="M12 28a18 18 0 0136 0" stroke="#fff" stroke-width="4" fill="none"/><rect x="8" y="24" width="8" height="14" rx="3" fill="#fff"/><rect x="44" y="24" width="8" height="14" rx="3" fill="#fff"/><path d="M48 38c0 6-8 8-14 8" stroke="#fff" stroke-width="3" fill="none"/></svg>
      <div><h3>Cutomer Care</h3><p>Talk Our Experts</p></div>
    </div>

    <div class="abs panel-head" style="top:694px">NEWSLETTER SIGN UP</div>
    <div class="abs newsletter">
      <p>Nemo enim ipsam voluptatem voluptas sit aspernatur aut oditaut.</p>
      <div class="email">ENTER EMAIL</div>
      <a class="subscribe" href="#">SUBSCRIBE</a>
    </div>
  </aside>

  <main>
    <section class="abs hero" role="img" aria-label="Promotional photo of a smiling woman in a colourful patterned sweater against a city skyline">
      <div class="hero-title"><span class="mega">MEGA</span><span class="sale">SALE</span></div>
      <div class="dots"><i class="on"></i><i></i><i></i><i></i></div>
    </section>

    <h2 class="abs section-title">Featured Collections</h2>

    <article class="abs card" style="left:324px">
      <div class="photo" role="img" aria-label="Model in a mint green dress" style="background:linear-gradient(#fff,#cdeee0 40%,#bfe6d6 80%,#fff)"></div>
      <h4>Product Name</h4>
      <p>Nemo enim ipsam voluptatem voluptas sit aspernatur aut oditaut.</p>
      <a class="shop" href="#">SHOP NOW</a>
    </article>
    <article class="abs card" style="left:578px">
      <div class="photo" role="img" aria-label="Model in a red and navy striped dress" style="background:linear-gradient(#fff,#d9434a 30%,#2c3550 60%,#d9434a 80%,#fff)"></div>
      <h4>Product Name</h4>
      <p>Nemo enim ipsam voluptatem voluptas sit aspernatur aut oditaut.</p>
      <a class="shop" href="#">SHOP NOW</a>
    </article>
    <article class="abs card" style="left:833px">
      <div class="photo" role="img" aria-label="Model in a white blouse and teal maxi skirt" style="background:linear-gradient(#fff,#f3efea 30%,#1f7a78 45%,#1a6a68 90%,#fff)"></div>
      <h4>Product Name</h4>
      <p>Nemo enim ipsam voluptatem voluptas sit aspernatur aut oditaut.</p>
      <a class="shop" href="#">SHOP NOW</a>
    </article>
  </main>

  <footer>
    <div class="abs footer"></div>
    <div class="abs foot-col" style="left:70px"><h5>Quick Links</h5><ul><li>Home</li><li>Featured Products</li><li>Specials</li><li>What's New</li><li>All Products ...</li></ul></div>
    <div class="abs foot-col" style="left:275px"><h5>Quick Links</h5><ul><li>About Us</li><li>Site Map</li><li>Gift Certificate FAQ</li><li>Discount Coupons</li><li>Newsletter Unsubscribe</li></ul></div>
    <div class="abs foot-col" style="left:481px"><h5>Customer Services</h5><ul><li>Contact Us</li><li>Shipping &amp; Returns</li><li>Privacy Notice</li><li>Conditions of Use</li><li>My Account</li></ul></div>
    <div class="abs foot-col" style="left:686px"><h5>Important Links</h5><ul><li>Store Locator</li><li>Social Media</li><li>Size Chart</li><li>Blog</li><li>Whole Sale Info</li></ul></div>
    <div class="abs foot-col social" style="left:888px"><h5>Connect Us</h5><ul>
      <li><i style="background:#3b5b98"></i>Friendwall</li>
      <li><i style="background:#4a9ad6"></i>Chirpline</li>
      <li><i style="background:#c8362f"></i>Pinboardly</li>
      <li><i style="background:#bbb"></i>Snapfold</li>
    </ul></div>
    <div class="abs copyright">Copyright © 2014. <b>FernQuill</b>. All Right Reserved</div>
  </footer>

</div>
</body>
</html>
```